We need a brochure designed for each of our 4 online training schools. All content will be supplied and most of the graphics. We have just had our websites rebranded and brochure needs to reflect the same design/brand....so we have a very clear design look for you to follow. Each brochure version will have very similar content...just different logos, links and images.

Brochure needs to have a click through table of contents and links to website within it. Example of brochure attached. We need the first of these asap....but we will need 3 more versions based on exactly the same layout over the coming 2 weeks.

Payment is now for one editable version of brochure.  With both working and finished file to be sent to us.

Industry/Entity Type

Training

```html
<!DOCTYPE html>
<html lang="en">
<head>
<meta charset="utf-8">
<title>Orchard Events – Course Brochure, Page 4</title>
<link rel="stylesheet" href="https://fonts.googleapis.com/css2?family=PT+Sans:ital,wght@0,400;0,700;1,400&display=swap">
<style>
  :root {
    --salmon: #f0876a;
    --salmon-soft: rgba(240, 135, 106, 0.92);
    --heading-ink: #3b1e16;
    --panel: rgba(0, 0, 0, 0.82);
    --button: #0d0d0d;
    --white: #ffffff;
    --rule: rgba(255, 255, 255, 0.85);
  }
  * { box-sizing: border-box; margin: 0; padding: 0; }
  html, body { width: 1200px; height: 848px; overflow: hidden; background: #e9e4df; }
  .page {
    position: relative;
    width: 1200px;
    height: 848px;
    overflow: hidden;
    font-family: "PT Sans", sans-serif;
  }
  .backdrop {
    position: absolute;
    inset: 0;
    background:
      radial-gradient(ellipse 320px 240px at 620px 330px, rgba(240, 150, 70, 0.75), transparent 70%),
      radial-gradient(ellipse 260px 220px at 470px 470px, rgba(70, 90, 40, 0.55), transparent 70%),
      radial-gradient(ellipse 300px 260px at 180px 640px, rgba(120, 110, 100, 0.45), transparent 70%),
      radial-gradient(ellipse 260px 300px at 1130px 300px, rgba(90, 80, 70, 0.4), transparent 70%),
      radial-gradient(ellipse 260px 200px at 980px 640px, rgba(230, 140, 100, 0.45), transparent 70%),
      linear-gradient(160deg, #d9d6d3 0%, #c9c2bc 45%, #d8cfc6 100%);
  }

  .brand-tab {
    position: absolute;
    left: 561px;
    top: 6px;
    height: 36px;
    display: flex;
    align-items: center;
    gap: 8px;
  }
  .brand-name {
    background: var(--white);
    color: var(--salmon);
    font-weight: 700;
    font-size: 11px;
    letter-spacing: 0.5px;
    padding: 10px 8px;
    text-transform: uppercase;
  }
  .page-number {
    border-left: 1px solid #555;
    padding-left: 6px;
    font-size: 13px;
    color: #333;
  }

  .divider {
    position: absolute;
    top: 122px;
    width: 2px;
    height: 623px;
    background: var(--rule);
  }

  .course {
    position: absolute;
    top: 77px;
    width: 310px;
  }
  .course--wedding-design { left: 92px; }
  .course--wedding-event { left: 446px; }
  .course--special-event { left: 800px; }

  .course__icon {
    display: block;
    width: 78px;
    height: 42px;
    margin: 0 auto 16px;
  }
  .course__title {
    background: var(--salmon-soft);
    color: var(--heading-ink);
    font-weight: 700;
    font-size: 19px;
    line-height: 26px;
    height: 55px;
    padding: 2px 8px 0;
    text-transform: uppercase;
  }
  .course__price {
    margin-top: 10px;
    background: var(--salmon-soft);
    color: var(--white);
    font-style: italic;
    font-size: 21px;
    line-height: 26px;
    height: 27px;
    padding: 0 9px;
  }
  .course__summary {
    margin-top: 11px;
    background: var(--panel);
    color: var(--white);
    font-size: 13.4px;
    line-height: 17.1px;
    padding: 19px 8px 8px 8px;
  }
  .course--wedding-design .course__summary { height: 456px; }
  .course--wedding-event .course__summary { height: 446px; padding-left: 20px; padding-right: 12px; }
  .course--special-event .course__summary { height: 439px; padding-left: 18px; padding-right: 12px; }

  .course__actions {
    position: absolute;
    top: 620px;
    left: 0;
    width: 310px;
    height: 50px;
    background: var(--salmon-soft);
    border-top: 1px solid var(--rule);
    border-bottom: 1px solid var(--rule);
    display: flex;
    justify-content: center;
    gap: 8px;
    align-items: center;
  }
  .course__button {
    width: 91px;
    height: 38px;
    background: var(--button);
    color: var(--salmon);
    font-size: 16px;
    display: flex;
    align-items: center;
    justify-content: center;
    text-decoration: none;
  }

  .contact-bar {
    position: absolute;
    left: 0;
    top: 770px;
    width: 1200px;
    height: 78px;
    background: var(--salmon);
  }
  .contact {
    position: absolute;
    top: 18px;
    display: flex;
    flex-direction: column;
    align-items: center;
    gap: 6px;
    color: var(--white);
    font-size: 13px;
    transform: translateX(-50%);
  }
  .contact--email { left: 408px; }
  .contact--phone { left: 622px; }
  .contact--chat { left: 836px; }
  .contact__icon { width: 17px; height: 17px; }
</style>
</head>
<body>
<div class="page">
  <div class="backdrop" role="img" aria-label="Soft-focus photograph of a wedding table with orange roses and place settings"></div>

  <div class="brand-tab">
    <span class="brand-name">Orchard Events</span>
    <span class="page-number">04</span>
  </div>

  <div class="divider" style="left:424px"></div>
  <div class="divider" style="left:777px"></div>

  <section class="course course--wedding-design">
    <svg class="course__icon" viewBox="0 0 78 42" aria-hidden="true">
      <polygon points="39,2 76,15 39,28 2,15" fill="#111"/>
      <path d="M18,21 L18,34 Q39,44 60,34 L60,21 L39,29 Z" fill="#111"/>
      <line x1="70" y1="17" x2="70" y2="32" stroke="#111" stroke-width="2"/>
      <rect x="68" y="31" width="4" height="7" fill="#111"/>
    </svg>
    <h2 class="course__title">Diploma in Wedding Planning, Styling and Design</h2>
    <p class="course__price">Get started for as little as £100</p>
    <div class="course__summary">
      <p>The Diploma in Wedding Planning, Styling and Design is the perfect course for those who want to combine a love of design with the planning elements of a wedding. It is a fast paced course that can be completed in as little as 6 months and covers all elements of design including applying colour, special effects, lighting and decor, as well as learning those crucial planning skills required to fully understand your client’s wedding. It allows them to not only plan the elements but design the overall concept using tools such as inspiration boards, design software and much more.</p>
      <p>The last two sections of your course, Sections 8 &amp; 9, are dedicated to marketing, starting and running a successful business in the wedding industry. These units will ensure you can hit the ground running upon successful completion of your course.</p>
      <p>Upon completion of the course you will receive a certificate which is bench marked at a Level 4 NVQ and be able to use the title of Certified Event Designer which is recognised internationally.</p>
    </div>
    <nav class="course__actions">
      <a class="course__button" href="#">read more</a>
      <a class="course__button" href="#">enquire</a>
      <a class="course__button" href="#">enrol online</a>
    </nav>
  </section>

  <section class="course course--wedding-event">
    <svg class="course__icon" viewBox="0 0 78 42" aria-hidden="true">
      <polygon points="39,2 76,15 39,28 2,15" fill="#111"/>
      <path d="M18,21 L18,34 Q39,44 60,34 L60,21 L39,29 Z" fill="#111"/>
      <line x1="70" y1="17" x2="70" y2="32" stroke="#111" stroke-width="2"/>
      <rect x="68" y="31" width="4" height="7" fill="#111"/>
    </svg>
    <h2 class="course__title">Diploma in Wedding<br>and Event Planning</h2>
    <p class="course__price">Get started for as little as £100</p>
    <div class="course__summary">
      <p>The Diploma in Wedding and Event Planning is the perfect course for those who want to plan, manage and produce both weddings and events for a living. It is a fast paced course that can be completed in as little as 6 months and covers all elements of planning festivals, conferences, pop-up events, weddings as outlined in the units below.</p>
      <p>The last two sections of your course, Sections 8 &amp; 9, are dedicated to marketing, finance and starting and running a successful business in the wedding and event industry. These units will ensure you can hit the ground running upon successful completion of your course.</p>
      <p>Upon completion of the course you will receive a diploma which is bench marked at a Level 4 NVQ and be able to use the title of Certified Wedding and Event Planner, which is recognised internationally.</p>
    </div>
    <nav class="course__actions">
      <a class="course__button" href="#">read more</a>
      <a class="course__button" href="#">enquire</a>
      <a class="course__button" href="#">enrol online</a>
    </nav>
  </section>

  <section class="course course--special-event">
    <svg class="course__icon" viewBox="0 0 78 42" aria-hidden="true">
      <polygon points="39,2 76,15 39,28 2,15" fill="#111"/>
      <path d="M18,21 L18,34 Q39,44 60,34 L60,21 L39,29 Z" fill="#111"/>
      <line x1="70" y1="17" x2="70" y2="32" stroke="#111" stroke-width="2"/>
      <rect x="68" y="31" width="4" height="7" fill="#111"/>
    </svg>
    <h2 class="course__title">Adv Dip in Special Event Planning and Design</h2>
    <p class="course__price">Get started for as little as £120</p>
    <div class="course__summary">
      <p>The Advanced Diploma in Planning and Design is the perfect course for someone wishing to work in all areas of events including weddings, corporate, festival, sporting, pop-up events as outlined in the units below. It is a fast paced course that can be completed in as little as 9 months and covers all elements in planning, managing, designing, styling and producing special events.</p>
      <p>The last two sections of your course, Sections 11 &amp; 12, are dedicated to marketing, finance, starting and running a successful business in the wedding and event industry. These units will ensure you can hit the ground running upon successful completion of your course.</p>
      <p>When you graduate you will receive a diploma which is bench marked at a Level 4 NVQ and be able to use the title of Certified Event Planner &amp; Designer, which is recognised internationally.</p>
    </div>
    <nav class="course__actions">
      <a class="course__button" href="#">read more</a>
      <a class="course__button" href="#">enquire</a>
      <a class="course__button" href="#">enrol online</a>
    </nav>
  </section>

  <footer class="contact-bar">
    <div class="contact contact--email">
      <svg class="contact__icon" viewBox="0 0 17 17" aria-hidden="true">
        <circle cx="8.5" cy="8.5" r="8.5" fill="#fff"/>
        <rect x="4" y="5.5" width="9" height="6.5" fill="none" stroke="#f0876a" stroke-width="1.2"/>
        <polyline points="4,5.5 8.5,9 13,5.5" fill="none" stroke="#f0876a" stroke-width="1.2"/>
      </svg>
      <span>hello@orchardevents.example</span>
    </div>
    <div class="contact contact--phone">
      <svg class="contact__icon" viewBox="0 0 17 17" aria-hidden="true">
        <circle cx="8.5" cy="8.5" r="8.5" fill="#fff"/>
        <path d="M6,4 L7.5,4 L8.2,6.4 L7.2,7.3 Q8,9.3 9.8,10 L10.7,9 L13,9.7 L13,11.2 Q12.5,12.8 10.5,12.4 Q5.2,10.8 4.6,6 Q4.6,4.3 6,4 Z" fill="#f0876a"/>
      </svg>
      <span>0800 555 0142.</span>
    </div>
    <div class="contact contact--chat">
      <svg class="contact__icon" viewBox="0 0 17 17" aria-hidden="true">
        <circle cx="8.5" cy="8.5" r="8.5" fill="#fff"/>
        <circle cx="8.5" cy="8.5" r="4" fill="none" stroke="#f0876a" stroke-width="1.4"/>
      </svg>
    </div>
  </footer>
</div>
</body>
</html>
```